Crumbs Crumbs - Home baking business needs a business card design. I sell at artisan food festivals.

A design for rebranding my baking business which serves artisan food festivals in the UK. Produce is locally sourced, homegrown or foraged, I make rustic unusual recipes. I would like a simple design using classic colours. I like green, 'Wrenby and Holt". I like chunky lettering, but very open to new ideas/designs. On the reverse side I would like a singular symbol demonstrating baking either a bowl and wooden spoon or cake and the facebook icon with CrumbsCrumbs

Reason: I would like to progress with the design by Tessa Marlow 4827305 . I misunderstood the deadline itinerary but would very much like to go ahead with your design. thanks

Target Market(s)

customers at food festivals, other small food businesses

Industry/Entity Type

Business

Contact Information for Business Card

Minimal amount of type on the card. Design to accentuate the look of my stall and style of baking . I display cakes on either old slate tiles, old palette boxes. Prices are hand written on brown luggage labels

Font styles to use
Other font styles liked:
• Blair MdiTC

Requirements
Must have
• Underneath Crumbs Crumbs i would like to have homemade by Pam somewhere on the front of the card.
Nice to have
• Clear lettering, classic colours i.e. Wrenby and Holt colour palettes.
Should not have
• Fancy, blingy, wordy,

```html
<!DOCTYPE html>
<html lang="en">
<head>
<meta charset="utf-8">
<title>Crumbs Crumbs – Business Card</title>
<link rel="stylesheet" href="https://fonts.googleapis.com/css2?family=Cinzel:wght@400&family=Sacramento&family=Varela+Round&display=swap">
<style>
  :root {
    --page-bg: #ecebe7;
    --mint-light: #a6dcc3;
    --mint: #86cfae;
    --mint-deep: #6fc3a0;
    --card-white: #fbfbfa;
    --ink: #4a4a4c;
    --icon: #5a5a5c;
    --apron-mint: #7ccfb0;
    --apron-ribbon: #e6a93a;
    --white: #ffffff;
  }
  * { box-sizing: border-box; margin: 0; padding: 0; }
  html, body { width: 1200px; height: 1000px; overflow: hidden; }
  body {
    background: var(--page-bg);
    position: relative;
  }
  .card {
    position: absolute;
    left: 250px;
    width: 700px;
    height: 400px;
    box-shadow: 0 6px 18px rgba(0,0,0,0.12);
  }
  .card-front {
    top: 70px;
    background:
      radial-gradient(ellipse at 45% 30%, var(--mint-deep) 0%, transparent 60%),
      radial-gradient(ellipse at 20% 80%, var(--mint-light) 0%, transparent 55%),
      linear-gradient(160deg, var(--mint-light), var(--mint) 55%, var(--mint-deep));
    text-align: center;
    color: var(--white);
  }
  .brand-name {
    font-family: "Cinzel", serif;
    font-weight: 400;
    font-size: 78px;
    line-height: 0.98;
    letter-spacing: 6px;
    padding-top: 92px;
  }
  .brand-tagline {
    font-family: "Sacramento", cursive;
    font-size: 50px;
    margin-top: 30px;
  }
  .card-back {
    top: 530px;
    background: var(--card-white);
    display: flex;
    align-items: center;
  }
  .apron-illustration {
    width: 180px;
    height: 270px;
    margin-left: 70px;
    border-radius: 40px 40px 90px 90px;
    background: linear-gradient(180deg, var(--apron-ribbon) 0%, var(--apron-mint) 18%, var(--apron-mint) 100%);
    opacity: 0.9;
  }
  .contact-list {
    list-style: none;
    margin-left: 70px;
    font-family: "Varela Round", sans-serif;
    font-size: 23px;
    color: var(--ink);
    letter-spacing: 1.5px;
  }
  .contact-item {
    display: flex;
    align-items: center;
    gap: 12px;
    margin: 18px 0;
  }
  .contact-icon { width: 22px; height: 22px; flex: none; }
</style>
</head>
<body>
  <section class="card card-front">
    <h1 class="brand-name">CRUMBS<br>CRUMBS</h1>
    <p class="brand-tagline">Homemade by Pam</p>
  </section>

  <section class="card card-back">
    <div class="apron-illustration" role="img" aria-label="Watercolour illustration of a mint green apron with golden ties"></div>
    <ul class="contact-list">
      <li class="contact-item">
        <svg class="contact-icon" viewBox="0 0 22 22" aria-hidden="true">
          <circle cx="11" cy="11" r="11" fill="var(--icon)"/>
          <path d="M7.5 5.5l2 2.5-1.2 1.4c.8 1.7 2 2.9 3.6 3.7l1.4-1.2 2.5 2-1.3 2c-4.6-.4-8.3-4.1-8.7-8.7z" fill="#fff"/>
        </svg>
        123-555-0142
      </li>
      <li class="contact-item">
        <svg class="contact-icon" viewBox="0 0 22 22" aria-hidden="true">
          <circle cx="11" cy="11" r="11" fill="var(--icon)"/>
          <rect x="5.5" y="7.5" width="11" height="7.5" fill="none" stroke="#fff" stroke-width="1.3"/>
          <path d="M5.5 7.5l5.5 4.2 5.5-4.2" fill="none" stroke="#fff" stroke-width="1.3"/>
        </svg>
        info@crumbscrumbs.com
      </li>
      <li class="contact-item">
        <svg class="contact-icon" viewBox="0 0 22 22" aria-hidden="true">
          <circle cx="11" cy="11" r="11" fill="var(--icon)"/>
        </svg>
        CRUMBSCRUMBS
      </li>
    </ul>
  </section>
</body>
</html>
```